Flyer promoting printing services to bars and restaurants

Small print company specialising in print for pubs, bard and restaurants looking for someone to design a flyer promoting our services which will be mailed to a database of potential customers. We have the text but need this putting into a nice design. The text is attached.

Ideally we would want separate versions - one for pubs / bars and another for restaurants.

Target Market(s)

Bars, pubs and restaurants

```html
<!DOCTYPE html>
<html lang="en">
<head>
<meta charset="utf-8">
<title>Harbour Print – Flyers for Bars and Restaurants</title>
<link rel="stylesheet" href="https://fonts.googleapis.com/css2?family=Bebas+Neue&family=Open+Sans:wght@400;600&family=Oswald:wght@500&family=Courgette&display=swap">
<style>
  :root {
    --stage: #2d2d2f;
    --white: #ffffff;
    --ink: #3a3a3a;
    --yellow: #f6d312;
    --font-head: "Bebas Neue", "Oswald", sans-serif;
    --font-body: "Open Sans", Arial, sans-serif;
    --font-brand: "Oswald", sans-serif;
    --font-script: "Courgette", cursive;
  }
  html, body { margin: 0; padding: 0; overflow: hidden; }
  body { width: 1200px; height: 776px; background: var(--stage); position: relative; font-family: var(--font-body); }

  .flyer {
    position: absolute; top: 38px; width: 495px; height: 700px;
    background: var(--white); overflow: hidden;
  }
  .flyer--bars {
    left: 75px;
    --tone-top: #3b2d80; --tone-side: #7a2b8e; --tone-main: #e0167c;
    --tone-accent: #f39200; --tone-hot: #e3122e; --tone-title: #7a2b8e;
    --tone-line: #7a2b8e;
    --photo: radial-gradient(circle at 40% 45%, #f7a21a 0%, #c4401f 22%, #5a2a40 48%, #221a2a 80%);
  }
  .flyer--restaurants {
    left: 630px;
    --tone-top: #ea5b1a; --tone-side: #e8701b; --tone-main: #d8131f;
    --tone-accent: #f39c12; --tone-hot: #e3122e; --tone-title: #d8131f;
    --tone-line: #d8131f;
    --photo: linear-gradient(160deg, #2a1208 0%, #e2591a 25%, #5a2b18 50%, #c9b58a 72%, #4a2a1c 100%);
  }

  .flyer__shapes { position: absolute; inset: 0; }
  .fill-top { fill: var(--tone-top); }
  .fill-side { fill: var(--tone-side); }
  .fill-main { fill: var(--tone-main); }
  .fill-accent { fill: var(--tone-accent); }
  .fill-hot { fill: var(--tone-hot); }
  .fill-yellow { fill: var(--yellow); }
  .fill-title { fill: var(--tone-title); }

  .brand { position: absolute; display: flex; align-items: center; gap: 8px;
    font-family: var(--font-brand); font-weight: 500; color: var(--ink); letter-spacing: 2px; }
  .brand__dot { display: block; background: var(--tone-main); }
  .brand--head { top: 22px; left: 26px; font-size: 24px; }
  .brand--head .brand__dot { width: 26px; height: 26px; }
  .brand--foot { top: 642px; left: 330px; font-size: 17px; }
  .brand--foot .brand__dot { width: 18px; height: 18px; }

  .intro { position: absolute; top: 92px; left: 24px; width: 255px; margin: 0;
    color: var(--white); font-size: 9.6px; line-height: 1.3; }

  .services { position: absolute; top: 222px; left: 36px; width: 252px; color: var(--white); }
  .services__title { margin: 0 0 10px; font-family: var(--font-head); font-weight: 400;
    font-size: 30px; line-height: 0.95; letter-spacing: 0.5px; }
  .services__list { list-style: none; margin: 0; padding: 0; }
  .services__item { margin-bottom: 9px; }
  .services__name { display: block; font-size: 13.5px; font-weight: 600; line-height: 1.15; }
  .services__note { display: block; font-size: 9.4px; line-height: 1.2; }

  .closing { position: absolute; top: 510px; left: 38px; width: 236px; margin: 0;
    padding: 12px 10px; border: 1.5px solid var(--white);
    color: var(--white); font-size: 10.6px; line-height: 1.35; }

  .title-box { position: absolute; top: 55px; left: 322px; width: 140px; height: 108px;
    border: 3px solid var(--white); box-sizing: border-box; display: flex; align-items: center; justify-content: center; }
  .title-box__text { margin: 0; font-family: var(--font-head); font-weight: 400; color: var(--white);
    font-size: 33px; line-height: 0.92; text-align: center; }
  .flyer--restaurants .title-box__text { font-size: 27px; }

  .photo { position: absolute; top: 250px; left: 300px; width: 195px; height: 232px; background: var(--photo); }
  .photo__frame { position: absolute; inset: 10px; border: 1.5px dashed var(--white); }
  .photo__note { position: absolute; left: 18px; right: 14px; bottom: 20px; margin: 0; padding: 8px;
    background: rgba(40,10,20,0.55); color: var(--white); font-family: var(--font-script);
    font-size: 11.5px; line-height: 1.3; text-align: center; }
  .flyer--restaurants .photo__note { top: 18px; bottom: auto; background: rgba(20,10,5,0.5); }

  .contacts { position: absolute; top: 505px; left: 318px; width: 162px; display: flex; flex-direction: column; gap: 14px; }
  .contact { position: relative; border: 1.5px solid var(--tone-line); padding: 5px 4px 4px;
    text-align: center; color: var(--tone-line); font-weight: 600; white-space: nowrap; }
  .contact__icon { position: absolute; top: -8px; left: 50%; width: 14px; height: 12px; margin-left: -7px;
    background: var(--white); }
  .contact__icon svg { display: block; width: 14px; height: 12px; fill: var(--tone-line); }
  .contact--phone { font-size: 16px; }
  .contact--email { font-size: 11.5px; }
  .contact--web { font-size: 12.5px; }
</style>
</head>
<body>

<!-- Bars flyer -->
<article class="flyer flyer--bars">
  <svg class="flyer__shapes" viewBox="0 0 495 700" aria-hidden="true">
    <polygon class="fill-top" points="0,82 300,48 300,300 0,300"/>
    <rect class="fill-side" x="0" y="300" width="300" height="400"/>
    <rect class="fill-main" x="22" y="212" width="278" height="488"/>
    <polygon class="fill-yellow" points="0,440 22,462 0,484"/>
    <polygon class="fill-hot" points="226,82 292,66 272,118"/>
    <rect class="fill-title" x="300" y="0" width="195" height="250"/>
    <polygon class="fill-top" points="300,0 345,0 300,110"/>
    <polygon class="fill-accent" points="345,250 495,60 495,250"/>
    <polygon class="fill-hot" points="300,455 345,482 300,482"/>
  </svg>

  <div class="brand brand--head"><span class="brand__dot"></span>HARBOUR PRINT</div>

  <p class="intro">Introducing Harbour Print, a Suffolk based printing company that prides itself on taking the personalised approach to our customer. We focus on specific sectors to ensure that we meet the requirements of our customers. Pubs and restaurants are one of the sectors in which we have a great deal of experience of providing print for.</p>

  <section class="services">
    <h2 class="services__title">Some of the printing<br>services we provide</h2>
    <ul class="services__list">
      <li class="services__item"><span class="services__name">Posters &amp; banners:</span><span class="services__note">Any size, indoor or outdoor, no minimum quantity, fast turnaround.</span></li>
      <li class="services__item"><span class="services__name">Branded / personalised clothing:</span><span class="services__note">T-shirts, polo-shirts, aprons, chefswear.</span></li>
      <li class="services__item"><span class="services__name">Menus:</span><span class="services__note">Printed sheets to insert into menu books or free standing folded menus. All formats.</span></li>
      <li class="services__item"><span class="services__name">Multi-part NCR order pads</span><span class="services__note">(no carbon required) and note pads.</span></li>
      <li class="services__item"><span class="services__name">Table talkers / tent cards</span></li>
      <li class="services__item"><span class="services__name">Flyers and leaflets</span></li>
    </ul>
  </section>

  <p class="closing">Whatever your requirements, Harbour Print offer a fast friendly service using the latest printing technology to produce high quality print. We also have our own in-house design studio and can help out with any design work if required.</p>

  <div class="title-box"><h1 class="title-box__text">Printing<br>services<br>for bars</h1></div>

  <div class="photo" role="img" aria-label="Photo of colourful cocktails on a bar counter">
    <div class="photo__frame"></div>
    <p class="photo__note">Please don't hesitate to get in touch and we would be happy to help. We never turn down an excuse to visit the bar!</p>
  </div>

  <div class="contacts">
    <div class="contact contact--phone"><span class="contact__icon"><svg viewBox="0 0 14 12"><path d="M3 1h2l1 3-1.5 1a7 7 0 0 0 3.5 3.5L9 7l3 1v2a1 1 0 0 1-1 1A10 10 0 0 1 2 2a1 1 0 0 1 1-1z"/></svg></span>01632 960418</div>
    <div class="contact contact--email"><span class="contact__icon"><svg viewBox="0 0 14 12"><path d="M1 2h12v8H1z M1 2l6 5 6-5" stroke="#fff" stroke-width="1"/></svg></span>sam@harbourprint.uk</div>
    <div class="contact contact--web"><span class="contact__icon"><svg viewBox="0 0 14 12"><circle cx="7" cy="6" r="5.5"/></svg></span>www.harbourprint.uk</div>
  </div>

  <div class="brand brand--foot"><span class="brand__dot"></span>HARBOUR PRINT</div>
</article>

<!-- Restaurants flyer -->
<article class="flyer flyer--restaurants">
  <svg class="flyer__shapes" viewBox="0 0 495 700" aria-hidden="true">
    <polygon class="fill-top" points="0,82 300,48 300,300 0,300"/>
    <rect class="fill-side" x="0" y="300" width="300" height="400"/>
    <rect class="fill-main" x="22" y="212" width="278" height="488"/>
    <polygon class="fill-yellow" points="0,440 22,462 0,484"/>
    <polygon class="fill-hot" points="226,82 292,66 272,118"/>
    <rect class="fill-title" x="300" y="0" width="195" height="250"/>
    <polygon class="fill-accent" points="300,0 360,0 300,120"/>
    <polygon class="fill-hot" points="400,250 495,90 495,250"/>
    <polygon class="fill-accent" points="300,455 345,482 300,482"/>
  </svg>

  <div class="brand brand--head"><span class="brand__dot"></span>HARBOUR PRINT</div>

  <p class="intro">Introducing Harbour Print, a Suffolk based printing company that prides itself on taking the personalised approach to our customer. We focus on specific sectors to ensure that we meet the requirements of our customers. Pubs and restaurants are one of the sectors in which we have a great deal of experience of providing print for.</p>

  <section class="services">
    <h2 class="services__title">Some of the printing<br>services we provide</h2>
    <ul class="services__list">
      <li class="services__item"><span class="services__name">Posters &amp; banners:</span><span class="services__note">Any size, indoor or outdoor, no minimum quantity, fast turnaround.</span></li>
      <li class="services__item"><span class="services__name">Branded / personalised clothing:</span><span class="services__note">T-shirts, polo-shirts, aprons, chefswear.</span></li>
      <li class="services__item"><span class="services__name">Menus:</span><span class="services__note">Printed sheets to insert into menu books or free standing folded menus. All formats.</span></li>
      <li class="services__item"><span class="services__name">Multi-part NCR order pads</span><span class="services__note">(no carbon required) and note pads.</span></li>
      <li class="services__item"><span class="services__name">Table talkers / tent cards</span></li>
      <li class="services__item"><span class="services__name">Flyers and leaflets</span></li>
    </ul>
  </section>

  <p class="closing">Whatever your requirements, Harbour Print offer a fast friendly service using the latest printing technology to produce high quality print. We also have our own in-house design studio and can help out with any design work if required.</p>

  <div class="title-box"><h1 class="title-box__text">Printing<br>services for<br>restaurants</h1></div>

  <div class="photo" role="img" aria-label="Photo of a grilled restaurant dish in front of flames">
    <div class="photo__frame"></div>
    <p class="photo__note">Please don't hesitate to get in touch and we would be happy to help. We never turn down an excuse to visit the restaurant!</p>
  </div>

  <div class="contacts">
    <div class="contact contact--phone"><span class="contact__icon"><svg viewBox="0 0 14 12"><path d="M3 1h2l1 3-1.5 1a7 7 0 0 0 3.5 3.5L9 7l3 1v2a1 1 0 0 1-1 1A10 10 0 0 1 2 2a1 1 0 0 1 1-1z"/></svg></span>01632 960418</div>
    <div class="contact contact--email"><span class="contact__icon"><svg viewBox="0 0 14 12"><path d="M1 2h12v8H1z M1 2l6 5 6-5" stroke="#fff" stroke-width="1"/></svg></span>sam@harbourprint.uk</div>
    <div class="contact contact--web"><span class="contact__icon"><svg viewBox="0 0 14 12"><circle cx="7" cy="6" r="5.5"/></svg></span>www.harbourprint.uk</div>
  </div>

  <div class="brand brand--foot"><span class="brand__dot"></span>HARBOUR PRINT</div>
</article>

</body>
</html>
```